Business Card Design

Very plain simple card, Plain modern font. Background. Grey fading to black. Large Bright lime green text. Saying.

TWR-ZA.COM

Small other details in white text.

Irish Horse Sales . Livery . Stud . Shows

Mark Dabrowski
TWR
Birch Lodge
Carrowmede Lane
Thistlecombe
Lincolnshire
LN4 7JX

Email. Twrzap@mailvale.co.uk
Tel. 07482 936504

Industry/Entity Type

Business

Contact Information for Business Card

As below

```html
<!DOCTYPE html>
<html lang="en">
<head>
<meta charset="utf-8">
<title>TWR-ZA.COM Business Card</title>
<link rel="stylesheet" href="https://fonts.googleapis.com/css2?family=Titillium+Web:wght@300;400;600;700&display=swap">
<style>
  :root {
    --page-bg: #d9dcdf;
    --card-grey: #3a3a3c;
    --card-black: #0e0e0f;
    --frame-line: rgba(0, 0, 0, 0.75);
    --lime: #4fb51a;
    --text-white: #f4f4f4;
    --text-soft: #d8d8d8;
  }
  * { box-sizing: border-box; margin: 0; padding: 0; }
  html, body {
    width: 1200px;
    height: 900px;
    overflow: hidden;
  }
  body {
    background: var(--page-bg);
    font-family: "Titillium Web", Arial, sans-serif;
    position: relative;
  }
  .business-card {
    position: absolute;
    left: 150px;
    top: 190px;
    width: 900px;
    height: 520px;
    background: radial-gradient(ellipse at 35% 25%, var(--card-grey) 0%, #222223 45%, var(--card-black) 100%);
    box-shadow: 0 10px 30px rgba(0, 0, 0, 0.35);
  }
  .card-frame {
    position: absolute;
    inset: 16px;
    border: 1.5px solid var(--frame-line);
  }
  .card-content {
    position: absolute;
    right: 70px;
    top: 52px;
    text-align: right;
    color: var(--text-white);
  }
  .brand-name {
    color: var(--lime);
    font-weight: 700;
    font-size: 62px;
    line-height: 1;
    letter-spacing: 1px;
  }
  .brand-name .brand-suffix {
    font-size: 46px;
  }
  .holder-name {
    margin-top: 14px;
    font-size: 36px;
    font-weight: 400;
    line-height: 1.1;
  }
  .services {
    margin-top: 6px;
    font-size: 22px;
    font-weight: 300;
    line-height: 1.2;
    color: var(--text-soft);
  }
  .contact-block {
    margin-top: 18px;
    display: flex;
    justify-content: flex-end;
    align-items: stretch;
    gap: 22px;
  }
  .contact-lines {
    font-size: 19px;
    font-weight: 300;
    line-height: 1.35;
    color: var(--text-soft);
  }
  .premises {
    font-weight: 600;
    color: var(--text-white);
  }
  .phone {
    margin-top: 14px;
    font-size: 20px;
    font-weight: 400;
    color: var(--text-white);
  }
  .accent-bar {
    width: 7px;
    background: var(--lime);
  }
  .email {
    margin-top: 16px;
    font-size: 20px;
    font-weight: 400;
    color: var(--text-white);
  }
</style>
</head>
<body>
  <section class="business-card">
    <div class="card-frame"></div>
    <div class="card-content">
      <div class="brand-name">TWR-ZA<span class="brand-suffix">.COM</span></div>
      <div class="holder-name">Mark Dabrowski</div>
      <div class="services">Irish Horse Sales<br>Livery . Stud . Shows</div>
      <div class="contact-block">
        <div class="contact-lines">
          <div class="premises">Birch Lodge</div>
          <div>Carrowmede Lane, Thistlecombe</div>
          <div>Lincolnshire, LN4 7JX</div>
          <div class="phone">07482 936504</div>
        </div>
        <div class="accent-bar"></div>
      </div>
      <div class="email">Twrzap@mailvale.co.uk</div>
    </div>
  </section>
</body>
</html>
```